Pals of Wagtail Fundraiser Flyer for shelter dogs

Flyer for Fund Raiser for shelter and rescue dogsThis will be hosted by who we are calling Heroes First responders (Fire, Police, and EMS will be bartending raising money to help the shelter dogs).

I will be uploading a basic flyer I did but I don't like it, only showing for dates and words etc...

struggling to come up with something eye-catching related to the above.

We can keep the use of Heroes (spelled wrong on the flyer)but open for new ideas too and new title.

Target Market(s)

Animal lovers

Font styles to use
Serif
Sans Serif

Requirements
Must have
• the ties to first responders and dog rescue
• Must include First responder logo badges images. The image with the helping hands Maybe replace the badges with images of dogs or doggy paws something like that
• Must have a strong presence identifying and relating to first responders
• Images of first responders as well as even images of the first responder logos for fire department police department and EMS.
• The first responders are the ones hosting the event so we really want to raise them up and show their appreciation for the cause that is super important as well
• Title should read
• Guardians Guarding Pups

```html
<!DOCTYPE html>
<html lang="en">
<head>
<meta charset="utf-8">
<title>Pals of Wagtail – Guardians Guarding Pups</title>
<link href="https://fonts.googleapis.com/css2?family=Anton&family=Montserrat:wght@300;400;700;800&family=Open+Sans:ital,wght@0,400;0,600;1,400;1,700&display=swap" rel="stylesheet">
<style>
  :root {
    --red: #e0121b;
    --red-dark: #b70d14;
    --black: #0b0b0b;
    --white: #ffffff;
    --ink: #1b1b1b;
    --backdrop: #e4e4e2;
  }
  * { box-sizing: border-box; margin: 0; padding: 0; }
  html, body { width: 1200px; height: 1200px; overflow: hidden; background: var(--backdrop); }
  .flyer {
    position: absolute; left: 200px; top: 15px; width: 800px; height: 1170px;
    background: var(--white); overflow: hidden; font-family: "Montserrat", sans-serif;
  }
  .photo { position: absolute; }
  .photo--bulldog { left: 0; top: 0; width: 205px; height: 390px;
    background: radial-gradient(ellipse at 55% 55%, #cfae82 0 30%, #f4efe8 62%, #fbfaf8 100%); }
  .photo--beagle { left: 565px; top: 0; width: 235px; height: 380px;
    background: radial-gradient(ellipse at 50% 50%, #b87a3e 0 20%, #e9e2d8 55%, #f7f6f4 100%); }
  .photo--volunteer { left: 30px; top: 402px; width: 222px; height: 420px;
    background: linear-gradient(160deg, #6f7f55 0%, #5a5044 35%, #3552a8 60%, #8a8f96 100%); }
  .photo--trainer { left: 262px; top: 492px; width: 318px; height: 330px;
    background: linear-gradient(150deg, #7f9a6c 0%, #8b8a86 40%, #d9c39a 70%, #5676a4 100%); }
  .photo--officer { left: 590px; top: 392px; width: 210px; height: 430px;
    background: linear-gradient(170deg, #7ea05a 0%, #3b4a34 35%, #1f2a44 65%, #55565a 100%); }

  .rule { position: absolute; background: var(--red); }
  .rule--left-v { left: 205px; top: 0; width: 8px; height: 395px; }
  .rule--left-h { left: 0; top: 390px; width: 213px; height: 7px; }
  .rule--right-v { left: 557px; top: 0; width: 8px; height: 392px; }
  .rule--right-h { left: 557px; top: 384px; width: 243px; height: 8px; }
  .rule--mid-v1 { left: 252px; top: 485px; width: 10px; height: 340px; }
  .rule--mid-v2 { left: 580px; top: 385px; width: 10px; height: 440px; }
  .rule--base { left: 30px; top: 822px; width: 770px; height: 7px; }

  .title-panel {
    position: absolute; left: 213px; top: 0; width: 344px; height: 485px;
    background: var(--black); border: 6px solid var(--red); border-top: 0;
    display: flex; flex-direction: column; align-items: center; color: var(--white);
  }
  .brand { margin-top: 48px; display: flex; flex-direction: column; align-items: center; gap: 12px; }
  .brand__mark { width: 96px; height: 96px; border-radius: 50%; background: var(--red); }
  .brand__name { font-weight: 700; font-size: 22px; color: var(--white); }
  .brand__sub { font-size: 9px; letter-spacing: 1px; color: #cfcfcf; margin-top: -6px; }
  .event-date { margin-top: 26px; font-weight: 700; font-size: 24px; letter-spacing: .5px; }
  .title-rule { width: 300px; height: 2px; background: var(--red); margin: 10px 0 6px; }
  .title { font-weight: normal; }
  .title__top { font-family: "Anton", sans-serif; font-size: 60px; line-height: 1; color: var(--red); letter-spacing: 1px; }
  .title__mid { display: flex; align-items: center; gap: 8px; margin-top: 6px; }
  .title__mid span { font-weight: 300; font-size: 32px; letter-spacing: 1px; }
  .stars { color: var(--red); font-size: 12px; letter-spacing: 1px; }
  .title__bottom { font-weight: 800; font-size: 58px; line-height: 1.05; letter-spacing: -1px; }

  .details { position: absolute; left: 30px; top: 850px; width: 770px; display: flex; }
  .details__time { flex: 0 0 250px; padding-left: 22px; border-right: 3px solid var(--red); white-space: nowrap; }
  .time { font-weight: 800; font-size: 50px; color: var(--red); line-height: 1; letter-spacing: -1px; }
  .host-label { font-family: "Open Sans", sans-serif; font-size: 19px; color: var(--ink); margin-top: 8px; }
  .venue { font-weight: 800; font-size: 22px; color: var(--red); }
  .details__copy { flex: 1 1 auto; padding: 0 40px 0 16px; font-family: "Open Sans", sans-serif; font-style: italic; }
  .lead { font-weight: 700; font-size: 21px; color: var(--red); }
  .body-copy { font-size: 15.5px; line-height: 1.45; color: var(--ink); margin-top: 4px; }

  .responder-badges { position: absolute; left: 240px; top: 1010px; display: flex; gap: 22px; }
  .badge { width: 90px; height: 90px; border-radius: 50%; background: radial-gradient(circle at 40% 35%, var(--red), var(--red-dark));
    display: flex; align-items: flex-end; justify-content: center; padding-bottom: 20px;
    color: var(--white); font-weight: 800; font-size: 15px; box-shadow: 0 2px 4px rgba(0,0,0,.25); }

  .footer { position: absolute; left: 0; bottom: 0; width: 800px; height: 52px; background: var(--black);
    display: flex; align-items: center; justify-content: space-between; padding: 0 40px;
    color: var(--white); font-family: "Open Sans", sans-serif; font-weight: 600; font-size: 15px; }
  .footer__item { display: flex; align-items: center; gap: 7px; }
  .dot { width: 12px; height: 12px; border-radius: 50%; background: var(--red); }
</style>
</head>
<body>
<main class="flyer">
  <div class="photo photo--bulldog" role="img" aria-label="Fawn French bulldog sitting on a white background"></div>
  <div class="photo photo--beagle" role="img" aria-label="Smiling beagle wearing a collar on a white background"></div>
  <div class="photo photo--volunteer" role="img" aria-label="Volunteer in a blue shirt kneeling beside a shepherd dog"></div>
  <div class="photo photo--trainer" role="img" aria-label="Man crouching to pet a yellow labrador guide dog"></div>
  <div class="photo photo--officer" role="img" aria-label="Police officer shaking paws with a black shepherd in a park"></div>

  <div class="rule rule--left-v"></div>
  <div class="rule rule--left-h"></div>
  <div class="rule rule--right-v"></div>
  <div class="rule rule--right-h"></div>
  <div class="rule rule--mid-v1"></div>
  <div class="rule rule--mid-v2"></div>
  <div class="rule rule--base"></div>

  <section class="title-panel">
    <div class="brand">
      <div class="brand__mark"></div>
      <div class="brand__name">Pals of Wagtail</div>
      <div class="brand__sub">RIVERBEND COUNTY DOG SHELTER</div>
    </div>
    <div class="event-date">AUG 15, 2019</div>
    <div class="title-rule"></div>
    <h1 class="title">
      <div class="title__top">GUARDIANS</div>
    </h1>
    <div class="title__mid"><b class="stars">★★★</b><span>GUARDING</span><b class="stars">★★★</b></div>
    <div class="title__bottom">PUPS</div>
    <div class="title-rule"></div>
  </section>

  <section class="details">
    <div class="details__time">
      <div class="time">6-10PM</div>
      <div class="host-label">Hosted at</div>
      <div class="venue">THE CEDAR HALL</div>
    </div>
    <div class="details__copy">
      <p class="lead">Join Pals of Wagtail for an evening of fun!</p>
      <p class="body-copy">Come spend an evening with our Celebrity Bartenders and help some pups in need our local men and women in uniform will be pouring drinks and raising awareness for adoption.</p>
    </div>
  </section>

  <div class="responder-badges">
    <div class="badge">FIRE</div>
    <div class="badge">POLICE</div>
    <div class="badge">EMS</div>
  </div>

  <footer class="footer">
    <div class="footer__item"><span class="dot"></span>@PalsOfWagtailRCDS</div>
    <div class="footer__item"><span class="dot"></span>www.palsofwagtail.org</div>
    <div class="footer__item"><span class="dot"></span>@powrcds</div>
  </footer>
</main>
</body>
</html>
```